Winelabel for Italian Wine incl. box.

Front and back label for new Italian wine.
It´s a premium redwine,
Size of Labels: Front 100x115 | Back 60x85
For front label we can also use these sizes:
95X115 - 100x100 – 86x97 – 100x110
For back labels : 60X90 – 60X95 – 60X100
We can only use one type of foil finishing.
BRAND = FIORALBA dal` Colle Brisco (in 2 lines)
2. titel = Calice di Sera
Semi lines = Ancient vinification Traditions | Truscany
Style = elegant Italian coloured Harlequin,
Other colors using white/black/gold
Include a round "water-mark" with text : Selected for loyal winelowers
Back label will be short story + legal data + barcode.
Outer box of 6 bottles case design print on all 4 fronts.

```html
<!DOCTYPE html>
<html lang="en">
<head>
<meta charset="utf-8">
<title>Fioralba dal` Colle Brisco – Front Label</title>
<link rel="stylesheet" href="https://fonts.googleapis.com/css2?family=Cinzel:wght@400;700&family=Montserrat:wght@600&display=swap">
<style>
  :root {
    --backdrop: #231f20;
    --label-paper: #fdfcfa;
    --label-blush: #faf3ee;
    --ink: #1a1a1a;
    --gold: #c6a447;
    --gold-light: #e3c878;
    --grey: #8f8f8f;
    --trim-line: #8a8a8a;
    --harlequin-green: #1f9a1f;
    --harlequin-red: #d90f0f;
  }
  * { margin: 0; padding: 0; box-sizing: border-box; }
  html, body {
    width: 1200px;
    height: 1130px;
    overflow: hidden;
    background: var(--backdrop);
  }
  .canvas {
    position: relative;
    width: 1200px;
    height: 1130px;
  }
  .trim-guide {
    position: absolute;
    left: 173px;
    top: 53px;
    width: 854px;
    height: 1024px;
    border: 2px dashed var(--trim-line);
  }
  .front-label {
    position: absolute;
    left: 190px;
    top: 70px;
    width: 820px;
    height: 990px;
    background: linear-gradient(90deg, var(--label-paper) 0%, var(--label-paper) 55%, var(--label-blush) 100%);
    text-align: center;
  }
  .harlequin-field {
    position: absolute;
    left: 272px;
    top: 166px;
    width: 299px;
    height: 281px;
    background: linear-gradient(90deg,
      var(--harlequin-green) 0%, #f6f3ea 33%, var(--harlequin-red) 50%,
      #1a7a1a 66%, #f6f3ea 83%, var(--harlequin-red) 100%);
    opacity: 0.85;
  }
  .brand-name {
    position: absolute;
    left: 0;
    width: 100%;
    top: 585px;
    font-family: "Cinzel", serif;
    font-weight: 400;
    font-size: 96px;
    line-height: 1;
    color: var(--ink);
    letter-spacing: 0.01em;
  }
  .brand-subline {
    position: absolute;
    left: 0;
    width: 100%;
    top: 700px;
    font-family: "Cinzel", serif;
    font-weight: 400;
    font-size: 60px;
    line-height: 1;
    color: var(--ink);
  }
  .loyalty-seal {
    position: absolute;
    left: 664px;
    top: 622px;
    width: 132px;
    height: 132px;
  }
  .wine-title {
    position: absolute;
    left: 0;
    width: 100%;
    top: 806px;
    font-family: "Cinzel", serif;
    font-weight: 700;
    font-size: 46px;
    line-height: 1;
    letter-spacing: 0.02em;
    background: linear-gradient(90deg, var(--gold) 0%, var(--gold-light) 40%, var(--gold) 70%, var(--gold-light) 100%);
    -webkit-background-clip: text;
    background-clip: text;
    color: transparent;
  }
  .tagline {
    position: absolute;
    left: 0;
    width: 100%;
    top: 887px;
    font-family: "Montserrat", sans-serif;
    font-weight: 600;
    font-size: 19px;
    line-height: 27px;
    letter-spacing: 0.32em;
    color: var(--grey);
  }
</style>
</head>
<body>
<main class="canvas">
  <div class="trim-guide"></div>
  <section class="front-label">
    <div class="harlequin-field" role="img" aria-label="Harlequin diamond pattern in green, white and red with gold outlines"></div>
    <h1 class="brand-name">FIORALBA</h1>
    <p class="brand-subline">dal` Colle Brisco</p>
    <svg class="loyalty-seal" viewBox="0 0 132 132" aria-hidden="true">
      <circle cx="66" cy="66" r="62" fill="none" stroke="#c9bc8e" stroke-width="2"/>
      <circle cx="66" cy="66" r="30" fill="none" stroke="#c9bc8e" stroke-width="1.5"/>
    </svg>
    <h2 class="wine-title">CALICE DI SERA</h2>
    <p class="tagline">ANCIENT VINIFICATION TRADITIONS<br>TUSCANY</p>
  </section>
</main>
</body>
</html>
```